Tri fold brochure for construction company

Looking for a tri fold brochure which utilizes black, teal and white colors. Logo must be on main page (several files with Logo attached)
Inside brochure.
1st Page - 3D photo/sketch/drawing of a complete residential high rise building with windows, balconies and elements of concrete and bricks.
2nd Page - Text which will outline company's main activities. file with text is attached.
3rd Page - photo/sketch/drawing of underground parking garage which shows columns/beams/walls/ and garage entrance/exit ramp. Can be multiple photos.
Back of brochure
1st page - company logo
2nd page - please propose something.
3rd page - company message with address and contact info (to be provided)
Back ground color of brochure should complement our logo/photos/sketches/drawings.
Alternative design options are welcome.

```html
<!DOCTYPE html>
<html lang="en">
<head>
<meta charset="utf-8">
<title>Northline Build Group – Tri-fold Brochure Outside</title>
<link href="https://fonts.googleapis.com/css2?family=Exo+2:wght@300;600;700;800&family=Open+Sans:wght@400;700&display=swap" rel="stylesheet">
<style>
  :root {
    --teal: #12a58c;
    --teal-dark: #0e8a75;
    --ink: #1b1b1b;
    --ink-soft: #2c2c2c;
    --paper: #ffffff;
    --paper-grey: #f1f1f1;
    --stage: #e4e4e4;
    --text: #2a2a2a;
  }
  * { margin: 0; padding: 0; box-sizing: border-box; }
  html, body { width: 837px; height: 1200px; overflow: hidden; background: var(--stage); }
  body { position: relative; font-family: "Open Sans", sans-serif; }

  .brochure {
    position: absolute; left: 18px; top: 289px;
    width: 800px; height: 622px;
    background: var(--paper);
    box-shadow: 0 10px 24px rgba(0,0,0,.18);
    overflow: hidden;
  }
  .panel { position: absolute; top: 0; height: 622px; overflow: hidden; }
  .panel svg.shapes { position: absolute; inset: 0; }

  /* Panel 1 – About */
  .panel-about { left: 0; width: 266px; background: linear-gradient(#fff, var(--paper-grey)); }
  .about-title {
    position: absolute; left: 17px; top: 22px;
    font-family: "Exo 2", sans-serif; font-weight: 800; font-size: 21px;
    color: var(--teal); letter-spacing: .2px;
    border-left: 2.5px solid var(--ink); padding-left: 8px; line-height: 18px;
  }
  .about-copy { position: absolute; left: 27px; top: 60px; width: 222px; }
  .body-text {
    font-size: 8.4px; line-height: 12.8px; color: var(--text);
    text-align: justify; hyphens: auto;
  }
  .body-text + .body-text { margin-top: 12px; }
  .body-text strong { font-weight: 700; color: var(--ink); }
  .web-tab {
    position: absolute; left: 36px; bottom: 0; width: 210px; height: 28px;
    background: var(--ink); border-radius: 12px 12px 0 0;
    color: #fff; font-size: 10.5px; text-align: center; line-height: 28px;
  }

  /* Panel 2 – Why choose / Contact */
  .panel-why { left: 266px; width: 264px; background: var(--ink); }
  .teal-sheet { position: absolute; left: 0; top: 9px; width: 254px; height: 603px; background: var(--teal); }
  .ribbon-label {
    position: absolute; left: 39px; top: 140px;
    transform: translate(-50%, -50%) rotate(-90deg);
    white-space: nowrap;
    font-family: "Exo 2", sans-serif; font-weight: 800; font-size: 15.5px;
    color: #fff; letter-spacing: .3px;
  }
  .why-copy { position: absolute; left: 76px; top: 45px; width: 168px; }
  .why-copy .body-text { color: #fff; text-align: left; font-size: 8.4px; line-height: 12.8px; }
  .contact-title {
    position: absolute; left: 0; width: 254px; top: 298px; text-align: center;
    font-family: "Exo 2", sans-serif; font-weight: 700; font-size: 17px; color: #fff;
  }
  .zigzag { position: absolute; left: 110px; top: 320px; }
  .contact-icons { position: absolute; left: 44px; top: 350px; display: flex; gap: 9px; }
  .contact-icons span {
    width: 32px; height: 32px; border-radius: 50%;
    background: var(--ink); border: 1.5px solid #fff;
    display: flex; align-items: center; justify-content: center;
  }
  .contact-lines {
    position: absolute; left: 0; width: 254px; top: 396px; text-align: center;
    font-family: "Exo 2", sans-serif; font-size: 8.4px; line-height: 11.8px; color: #fff;
  }
  .contact-lines .gap { margin-top: 7px; }
  .brand-box {
    position: absolute; left: 44px; top: 499px; width: 167px; height: 86px;
    border: 1px solid rgba(255,255,255,.75); border-radius: 3px;
    background: rgba(255,255,255,.08);
    display: flex; flex-direction: column; align-items: center; justify-content: center; gap: 6px;
  }
  .brand-mark { width: 12px; height: 12px; background: var(--ink); }
  .brand-name {
    font-family: "Exo 2", sans-serif; font-weight: 700; font-size: 15px;
    color: var(--ink); letter-spacing: .5px; text-align: center; line-height: 17px;
  }

  /* Panel 3 – Cover */
  .panel-cover { left: 530px; width: 270px; background: var(--ink); }
  .cover-brand {
    position: absolute; left: 0; width: 270px; top: 62px;
    display: flex; flex-direction: column; align-items: center; gap: 10px;
  }
  .cover-brand .brand-mark { width: 16px; height: 16px; background: var(--teal); }
  .cover-brand .brand-name { color: #fff; font-size: 20px; line-height: 23px; }
  .cover-tagline { position: absolute; left: 0; width: 270px; top: 486px; text-align: center; }
  .tag-small {
    font-family: "Exo 2", sans-serif; font-weight: 300; font-size: 16px;
    color: var(--ink); letter-spacing: .3px; line-height: 18px;
  }
  .tag-teal {
    font-family: "Exo 2", sans-serif; font-weight: 700; font-size: 29px;
    color: var(--teal); line-height: 29px;
  }
  .tag-dark {
    font-family: "Exo 2", sans-serif; font-weight: 800; font-size: 31px;
    color: var(--ink); line-height: 31px;
  }
  .cover-web {
    position: absolute; left: 0; width: 270px; top: 593px; text-align: center;
    font-size: 9.5px; color: var(--ink);
  }
  .cover-web i {
    display: inline-block; width: 9px; height: 9px; border-radius: 50%;
    border: 1.5px solid var(--ink); vertical-align: -1px; margin-right: 5px;
  }
</style>
</head>
<body>
<main class="brochure">

  <!-- Panel 1: About us -->
  <section class="panel panel-about">
    <svg class="shapes" width="266" height="622" viewBox="0 0 266 622">
      <defs>
        <linearGradient id="dig-site" x1="0" y1="0" x2="0" y2="1">
          <stop offset="0" stop-color="#7fa6cf"/>
          <stop offset=".45" stop-color="#b9c7d6"/>
          <stop offset=".6" stop-color="#c9622a"/>
          <stop offset="1" stop-color="#8a6a48"/>
        </linearGradient>
      </defs>
      <polygon points="0,327 266,410 266,622 0,622" fill="url(#dig-site)" role="img" aria-label="Photo of an orange excavator on a dirt construction site under blue sky"/>
      <polygon points="170,380 266,330 266,410" fill="var(--ink)"/>
    </svg>
    <h2 class="about-title">ABOUT US</h2>
    <div class="about-copy">
      <p class="body-text"><strong>Lorem Ipsum is simply dummy text</strong> of the printing and typesetting industry. Lorem Ipsum has been the industry's standard dummy text ever since the 1500s, when an unknown printer took a galley of type and scrambled it to make a type specimen book. It has survived not only five centuries, but also the leap into electronic typesetting, remaining essentially unchanged. It was popularised in the 1960s with the release of Letraset sheets containing Lorem Ipsum passages, and more recently with desktop publishing software like Aldus PageMaker including versions of Lorem Ipsum.</p>
      <p class="body-text"><strong>Lorem Ipsum is simply dummy text</strong> of the printing and typesetting industry. Lorem Ipsum has been the industry's standard dummy text ever since the 1500s, when an unknown printer took a galley of type and scrambled it to make a type specimen book. It has survived not only five centuries, but also the leap into electronic typesetting, remaining essentially.</p>
    </div>
    <div class="web-tab">www.northlinebuild.com</div>
  </section>

  <!-- Panel 2: Why choose / Contact -->
  <section class="panel panel-why">
    <div class="teal-sheet"></div>
    <svg class="shapes" width="264" height="622" viewBox="0 0 264 622">
      <polygon points="18,0 60,0 60,282 39,293 18,282" fill="var(--ink)"/>
    </svg>
    <h2 class="ribbon-label">WHY CHOOSE NORTHLINE</h2>
    <div class="why-copy">
      <p class="body-text">Lorem Ipsum is simply dummy text of the printing and typesetting industry. Lorem Ipsum has been the industry's standard dummy text ever since the 1500s, when an unknown printer took a galley of type and scrambled it to make a type specimen book. It has survived not only five centuries, but also the leap into electronic typesetting, remaining essentially unchanged. It was popularised in the 1960s with the release of Letraset sheets containing Lorem Ipsum passages, and more recently with desktop publishing software like Aldus PageMaker including versions of Lorem Ipsum.</p>
    </div>
    <h2 class="contact-title">CONTACT US</h2>
    <svg class="zigzag" width="34" height="6" viewBox="0 0 34 6">
      <polyline points="0,5 3,1 6,5 9,1 12,5 15,1 18,5 21,1 24,5 27,1 30,5 33,1" fill="none" stroke="var(--ink)" stroke-width="1.6"/>
    </svg>
    <div class="contact-icons">
      <span aria-label="Address"><svg width="16" height="16" viewBox="0 0 16 16" fill="none" stroke="#fff" stroke-width="1.2"><path d="M2 8 8 2.5 14 8M4 7v6.5h8V7M7 13.5V10h2v3.5"/></svg></span>
      <span aria-label="Mobile"><svg width="16" height="16" viewBox="0 0 16 16" fill="none" stroke="#fff" stroke-width="1.2"><rect x="5" y="1.5" width="6" height="13" rx="1"/><line x1="7" y1="12.5" x2="9" y2="12.5"/></svg></span>
      <span aria-label="Phone"><svg width="16" height="16" viewBox="0 0 16 16" fill="none" stroke="#fff" stroke-width="1.2"><path d="M3 2.5h3l1 3-1.7 1.2a8 8 0 0 0 4 4L10.5 9l3 1v3a1 1 0 0 1-1 1A11 11 0 0 1 2 3.5a1 1 0 0 1 1-1z"/></svg></span>
      <span aria-label="Email"><svg width="16" height="16" viewBox="0 0 16 16" fill="none" stroke="#fff" stroke-width="1.2"><rect x="2" y="4" width="12" height="8.5"/><path d="M2 4l6 5 6-5"/></svg></span>
    </div>
    <div class="contact-lines">
      <p>A-123 Lorem Ipsum is simply, Lorem<br>Ipsum is simply R12 345</p>
      <p class="gap">123-456-7890 &nbsp;|&nbsp; 123-456-7891</p>
      <p>info@northlinebuild.com</p>
    </div>
    <div class="brand-box">
      <span class="brand-mark"></span>
      <p class="brand-name">NORTHLINE<br>BUILD GROUP</p>
    </div>
  </section>

  <!-- Panel 3: Cover -->
  <section class="panel panel-cover">
    <svg class="shapes" width="270" height="622" viewBox="0 0 270 622">
      <defs>
        <linearGradient id="crew" x1="0" y1="0" x2="1" y2="1">
          <stop offset="0" stop-color="#e0a93a"/>
          <stop offset=".45" stop-color="#c9d6e6"/>
          <stop offset="1" stop-color="#e9edf2"/>
        </linearGradient>
      </defs>
      <polygon points="0,150 270,134 270,420 0,500" fill="url(#crew)" role="img" aria-label="Photo of a smiling construction worker in a white hard hat with crew and yellow machinery behind"/>
      <polygon points="0,490 270,395 270,420 0,515" fill="var(--ink)"/>
      <polygon points="0,510 270,412 270,622 0,622" fill="var(--paper)"/>
      <g stroke="var(--teal)" stroke-width="3.5">
        <polygon points="42,415 66,429 66,457 42,471 18,457 18,429" fill="#b7c4b0" role="img" aria-label="Photo of a finished suburban house"/>
        <polygon points="118,392 145,407 145,439 118,454 91,439 91,407" fill="#d7673a" role="img" aria-label="Photo of work gloves and tools"/>
        <polygon points="196,370 222,385 222,415 196,430 170,415 170,385" fill="#d9d2c0" role="img" aria-label="Photo of hands reviewing building plans"/>
      </g>
    </svg>
    <div class="cover-brand">
      <span class="brand-mark"></span>
      <p class="brand-name">NORTHLINE<br>BUILD GROUP</p>
    </div>
    <div class="cover-tagline">
      <p class="tag-small">A SUPERIOR</p>
      <p class="tag-teal">CONSTRUCTION</p>
      <p class="tag-dark">EXPERIENCE</p>
    </div>
    <p class="cover-web"><i></i>www.northlinebuild.com</p>
  </section>

</main>
</body>
</html>
```